Flock and co fleece works pty ltd

We are sheep shearing contractors,we are looking for a simple design business card, with a drawing like picture of a Australian sheep on it, then just standard details, name, phone, email, po box.
We would like double sided, with 2 lines of wiriting on the back, no bright colours please.
We like black and white, doesn't have to be too serious, however nothing to far left of cwntre.
On the back of the card we would like professional shearing contract offering full contract team.
Can use use the symbol & in the name instead of and.

Target Market(s)

Sheep farmers, target males from age 20 and up

Contact Information for Business Card

Company name flock and co fleece works pty ltd
Darren holloway 0491352706, po box 4071 sale vic 3853,
Email flockandcofleece@mailbarn.example, gippsland shearing contractor

Font styles to use
Serif

Colors

Designer to choose only greyscale colors for use in the design.

Requirements
Nice to have
• Simple design

```html
<!DOCTYPE html>
<html lang="en">
<head>
<meta charset="utf-8">
<title>Flock &amp; Co Fleece Works – Business Card</title>
<link rel="stylesheet" href="https://fonts.googleapis.com/css2?family=Tinos:wght@400;700&display=swap">
<style>
  :root {
    --backdrop: #cfcbc6;
    --card-white: #ffffff;
    --card-black: #0b0b0b;
    --ink: #111111;
    --ink-soft: #2a2a2a;
    --paper-text: #f2f2f2;
    --illustration-tone: #3a3a3a;
    --sheep-tone-light: #ececec;
    --sheep-tone-mid: #d6d6d6;
    --card-shadow: rgba(0, 0, 0, 0.35);
  }
  * { box-sizing: border-box; margin: 0; padding: 0; }
  html, body { width: 900px; height: 1200px; overflow: hidden; }
  body {
    background: var(--backdrop);
    font-family: "Tinos", "Times New Roman", serif;
    position: relative;
  }
  .card {
    position: absolute;
    left: 80px;
    width: 735px;
    height: 430px;
    border-radius: 28px;
    overflow: hidden;
    box-shadow: 0 6px 18px var(--card-shadow);
  }
  .card--front { top: 127px; background: var(--card-white); color: var(--ink); }
  .card--back {
    top: 645px;
    background: radial-gradient(ellipse at 50% 40%, #1c1c1c 0%, var(--card-black) 70%);
    color: var(--paper-text);
  }

  /* front */
  .shearer-illustration {
    position: absolute; left: 44px; top: 38px; width: 146px; height: 170px;
    background: linear-gradient(160deg, #5a5a5a, var(--illustration-tone));
    border-radius: 6px;
    opacity: 0.85;
  }
  .sheep-photo {
    position: absolute; left: 500px; top: 14px; width: 190px; height: 405px;
    background: linear-gradient(180deg, var(--sheep-tone-light), var(--sheep-tone-mid) 55%, var(--sheep-tone-light));
    border-radius: 40px 40px 10px 10px;
    opacity: 0.8;
  }
  .brand { position: absolute; text-transform: uppercase; font-weight: 400; line-height: 1; white-space: nowrap; }
  .card--front .brand { left: 178px; top: 108px; color: var(--ink); }
  .brand__name { display: block; font-size: 56px; letter-spacing: 2px; }
  .brand__tagline { display: block; font-size: 17px; letter-spacing: 1px; margin-top: 6px; }

  .role { position: absolute; left: 42px; top: 314px; }
  .role__title { font-size: 17px; font-weight: 700; letter-spacing: 0.3px; }
  .role__name { font-size: 16px; margin-top: 5px; text-transform: uppercase; }

  .divider { position: absolute; left: 415px; top: 316px; width: 1.5px; height: 62px; background: var(--ink); }

  .contact-list { position: absolute; left: 436px; top: 314px; list-style: none; }
  .contact-list li { display: flex; align-items: center; height: 23.5px; font-size: 15.5px; color: var(--ink-soft); }
  .contact-list svg { width: 15px; height: 15px; margin-right: 10px; flex: none; }

  /* back */
  .card--back .brand { left: 0; right: 0; top: 96px; text-align: center; color: var(--paper-text); }
  .card--back .brand__name { font-size: 60px; }
  .card--back .brand__tagline { font-size: 18px; margin-top: 8px; }

  .offering { position: absolute; left: 0; right: 0; top: 210px; text-align: center; }
  .offering__title { font-size: 18px; font-weight: 700; letter-spacing: 0.4px; }
  .offering__line { font-size: 17px; margin-top: 3px; }
  .offering__dot { margin: 0 6px; }
  .owners { position: absolute; left: 0; right: 0; top: 314px; text-align: center; font-size: 15px; }
</style>
</head>
<body>

  <section class="card card--front">
    <div class="shearer-illustration" role="img" aria-label="Line drawing of a shearer bent over a sheep"></div>
    <div class="sheep-photo" role="img" aria-label="Faded photograph of a standing merino sheep"></div>

    <div class="brand">
      <span class="brand__name">Flock &amp; Co</span>
      <span class="brand__tagline">Fleece Works Pty Ltd</span>
    </div>

    <div class="role">
      <p class="role__title">GIPPSLAND SHEARING CONTRACTOR</p>
      <p class="role__name">Darren Holloway</p>
    </div>

    <div class="divider"></div>

    <ul class="contact-list">
      <li>
        <svg viewBox="0 0 16 16" aria-hidden="true"><circle cx="8" cy="8" r="8" fill="#111"/><path d="M5.2 4.2l1.4-.3.8 1.9-.9.7a5 5 0 0 0 2.9 2.9l.7-.9 1.9.8-.3 1.4c-3.5.3-6.8-3-6.5-6.5z" fill="#fff"/></svg>
        0491352706
      </li>
      <li>
        <svg viewBox="0 0 16 16" aria-hidden="true"><circle cx="8" cy="8" r="8" fill="#111"/><rect x="4" y="5" width="8" height="6" rx="0.8" fill="#fff"/><path d="M4.3 5.4L8 8.3l3.7-2.9" stroke="#111" stroke-width="0.9" fill="none"/></svg>
        Po Box 4071 Sale Vic 3853
      </li>
      <li>
        <svg viewBox="0 0 16 16" aria-hidden="true"><circle cx="8" cy="8" r="8" fill="#111"/><path d="M8 3.4a3 3 0 0 0-3 3c0 2.2 3 5.6 3 5.6s3-3.4 3-5.6a3 3 0 0 0-3-3z" fill="#fff"/><circle cx="8" cy="6.4" r="1.1" fill="#111"/></svg>
        flockandcofleece@mailbarn.example
      </li>
    </ul>
  </section>

  <section class="card card--back">
    <div class="brand">
      <span class="brand__name">Flock &amp; Co</span>
      <span class="brand__tagline">Fleece Works Pty Ltd</span>
    </div>

    <div class="offering">
      <p class="offering__title">ORGANISED SHEARING SERVICE OFFERING</p>
      <p class="offering__line">Full contract team<span class="offering__dot">•</span>Shearers<span class="offering__dot">•</span>Rousies<span class="offering__dot">•</span>Classer<span class="offering__dot">•</span>Wool Press</p>
      <p class="offering__line">2 stand mobile shearing/Crutching trailier</p>
    </div>

    <p class="owners">Darren &amp; Lisa Holloway</p>
  </section>

</body>
</html>
```